Flyer Needed to Advertise New Online Reading Programs

ABOUT THE TRUST OF READING DEVELOPMENT
The Trust teaches summer reading skills programs for elementary school students, in programs offered through partnerships with universities, colleges and municipalities nationwide. The goal of each program is to build reading skills, and to foster a lifetime love of books and reading.

AIMS & TARGET MARKET
The Trust has developed a new format of its’ online reading program for elementary students, which includes live small-group video classes taught by a professional reading teacher. The Trust seeks a new graphic design for a flyer to advertise the new online reading program. The flyer will be sent to elementary schools, passed out by teachers, and then taken home by students to show parents; therefore, the primary audience for the flyer will be teachers and parents of elementary school students.

Live classes for children are completely new in online education, unlike anything else in the marketplace, and parents and teachers therefore have no experience with them. The successful design will include illustrations or photographs that allow visitors to immediately grasp/understand the new video class format, without relying heavily on a written description. Additionally, the successful flyer concept will make the program, and the video classes in particular, feel fun and appealing to kids and parents.

Below is additional information about the new live small-group video class format, which meets weekly for 6 weeks:
o During video classes, students participate from home.
o During discussions, the student’s computer (or tablet) screen is filled with live video frames of the teacher and the other students. The video frame for the teacher is larger, and the other students appear in smaller frames.
o During other video class instruction, the teacher uses a presentation screen to display pages of a book or a “whiteboard” used for instructional activities.

Notes: The flyer design could include an illustrated or photo screenshot of a video class, with children looking engaged and a teacher leading them in discussion (stock photos are okay to use in flyer design). We have included a screen shot of one of these classes for reference, but do not feel constrained to represent this screen realistically (as shown here). Layout, look and feel can be changed. Alternatively, you may choose to use a graphic other than a screenshot to bring across the concept of the video classes.

COPY AND SPECIFICATIONS
The flyer design will be one-sided and the dimensions are 8.5” x 11” in either portrait or landscape orientation. We will consider designs in color or black and white. Since we brand our flyers with logos of the universities we partner with throughout the nation, we’ll need to include a partner logo in the design. Exact copy will be provided, but layout is flexible. Screenshots from our sample classes are included to show screen layout. Stock photos are okay to use in flyer designs.

Reason: We'd like to make edits to existing designs.

Hi designers, We wanted to share our thoughts on the main image of the flyer. We're leaning towards an image that shows a sole student on a computer with the computer screen in view. The computer screen could have the sample image we provided to show how the video classes operate. Thanks! The Trust of Reading Development

Graphic Design

```html
<!DOCTYPE html>
<html lang="en">
<head>
<meta charset="utf-8">
<title>Reading Skills Classes — Online this Summer</title>
<link rel="stylesheet" href="https://fonts.googleapis.com/css2?family=Nunito:wght@800;900&family=Cardo:wght@400;700&family=Arimo:wght@400;700&display=swap">
<style>
  :root {
    --green: #1f5810;
    --yellow: #f8ec1c;
    --yellow-btn: #fde21a;
    --ink: #111111;
    --white: #ffffff;
    --book-dark: #3a1f12;
    --book-warm: #b8773f;
    --book-light: #e9d3ad;
  }
  * { margin: 0; padding: 0; box-sizing: border-box; }
  html, body { width: 1200px; height: 927px; overflow: hidden; background: #ffffff; }
  .flyer { position: relative; width: 1200px; height: 927px; overflow: hidden; }

  .hero {
    position: absolute; left: 0; top: 0; width: 1200px; height: 384px;
    background:
      radial-gradient(ellipse at 50% 95%, var(--book-light) 0%, var(--book-warm) 35%, transparent 65%),
      linear-gradient(90deg, #5b2a18 0%, var(--book-dark) 30%, #2a1710 60%, #6b4a2c 100%);
  }
  .hero-photo { position: absolute; left: 633px; width: 209px; }
  .photo-reader { top: 0; height: 123px; background: linear-gradient(135deg, #6e3a1c, #2b1408 70%); }
  .photo-video { top: 130px; height: 139px; background: linear-gradient(180deg, #1d2b33, #0c1418); }
  .photo-classroom { top: 276px; height: 102px; background: linear-gradient(135deg, #8fb3c9, #d7c2b0); }

  .partner-name {
    position: absolute; left: 248px; top: 30px;
    font-family: "Cardo", serif; font-weight: 700; font-size: 21px; color: var(--white);
    white-space: nowrap;
  }

  .title {
    position: absolute; left: 38px; top: 74px;
    font-family: "Nunito", sans-serif; font-weight: 900; font-size: 53px; letter-spacing: 0.4px;
    color: var(--white); text-shadow: 2px 3px 4px rgba(0,0,0,0.8); white-space: nowrap;
  }
  .badge {
    position: absolute; left: 140px; top: 143px; width: 353px; height: 74px;
    background: var(--yellow-btn); border: 4px solid #3a3a3a; border-radius: 10px;
    display: flex; align-items: center; justify-content: center;
    font-family: "Arimo", sans-serif; font-weight: 700; font-size: 27px; color: var(--ink);
  }
  .features {
    position: absolute; left: 38px; top: 264px; list-style: none; white-space: nowrap;
    font-family: "Cardo", serif; font-weight: 700; font-size: 23px; line-height: 24.5px;
    letter-spacing: 0.8px; color: var(--white);
    text-shadow: 1px 1px 3px rgba(0,0,0,0.9);
  }
  .features li::before { content: "• "; }

  .skills {
    position: absolute; left: 846px; top: 76px;
    font-family: "Nunito", sans-serif; font-weight: 900; color: var(--white);
    text-shadow: 2px 2px 3px rgba(0,0,0,0.85);
  }
  .skills h2 { font-size: 33px; font-weight: 900; margin-left: 5px; letter-spacing: 1px; white-space: nowrap; line-height: 40px; }
  .skills ul { list-style: none; margin-top: 0; }
  .skills li { font-size: 31px; line-height: 36.5px; display: flex; align-items: center; white-space: nowrap; }
  .skills li::before {
    content: ""; width: 21px; height: 21px; border-radius: 50%; background: var(--white);
    margin-right: 8px; flex: none;
  }

  .programs {
    position: absolute; left: 0; top: 384px; width: 1200px; height: 472px; overflow: hidden;
    background: var(--green); color: var(--white);
    font-family: "Cardo", serif; padding: 8px 40px 0 40px;
  }
  .programs h3 { font-size: 21px; font-weight: 400; letter-spacing: 1px; margin-bottom: 10px; white-space: nowrap; }
  .program { margin-bottom: 14.6px; font-size: 16px; line-height: 15.4px; letter-spacing: 0.9px; white-space: nowrap; }
  .program h4 { font-size: 16px; font-weight: 400; }

  .contact {
    position: absolute; left: 0; top: 856px; width: 1200px; height: 71px;
    background: var(--yellow); color: var(--ink);
    font-family: "Arimo", sans-serif; font-size: 25px; line-height: 23px; text-align: center;
    padding-top: 6px; white-space: nowrap;
  }
</style>
</head>
<body>
<main class="flyer">
  <section class="hero" role="img" aria-label="Open books and stacks of books on shelves"></section>
  <div class="hero-photo photo-reader" role="img" aria-label="A young woman reading a book in a warm-lit room"></div>
  <div class="hero-photo photo-video" role="img" aria-label="A video class screen with the teacher in a large frame and students in small frames"></div>
  <div class="hero-photo photo-classroom" role="img" aria-label="A teacher helping two children at a computer"></div>

  <div class="partner-name">Alderbrook University</div>

  <h1 class="title">Reading Skills Classes</h1>
  <div class="badge">Online this Summer!</div>

  <ul class="features">
    <li>Small class size</li>
    <li>A skilled and encouraging teacher</li>
    <li>Individualized skills instruction</li>
    <li>A program of independent reading in great books</li>
  </ul>

  <div class="skills">
    <h2>READING SKILLS:</h2>
    <ul>
      <li>Phonics</li>
      <li>Comprehension</li>
      <li>Fluency</li>
      <li>Study Skills</li>
      <li>Speed Reading</li>
      <li>Love of Reading</li>
    </ul>
  </div>

  <section class="programs">
    <h3>PROGRAM DESCRIPTIONS:</h3>
    <div class="program"><h4>Program for Preschoolers:</h4>Students in this program build strong reading readiness skills. Your child will learn letter recognition and beginning phonics, and develop<br>the motivation and love of reading that make learning to read easy, enjoyable, and successful.</div>
    <div class="program"><h4>Program for Entering Kindergartners:</h4>Students in this program learn beginning reading skills and develop a love of books. Your child will learn letter recognition, phonics,<br>and sight words, and will learn to sound out short words.</div>
    <div class="program"><h4>Program for Entering 1st Graders:</h4>Students in this program learn to read independently. Your child will learn phonics and sight words, build comprehension, and gain the skills<br>and confidence needed for success in first grade.</div>
    <div class="program"><h4>Program for Entering 2nd Graders:</h4>Students in this program become fluent, independent readers. Your child will make significant gains in phonics and word-attack skills, fluency,<br>and comprehension, and will develop confidence and a love of reading.</div>
    <div class="program"><h4>Program for Entering 3rd Graders:</h4>Students in this program become strong independent readers. Your child will develop the comprehension, fluency, and long-word decoding<br>skills needed to read longer books with ease, and will build confidence and a love of reading.</div>
    <div class="program"><h4>Program for Entering 4th and 5th Graders:</h4>Students in this program make substantial gains in comprehension, long-word decoding skills, fluency, and reading speed. Your child will<br>complete homework more quickly and easily, be more successful in school, and become a strong, enthusiastic reader.</div>
    <div class="program"><h4>Programs for Entering 6th-8th Graders and Entering 9th and 10th Graders:</h4>Students in these programs make substantial gains in comprehension while doubling reading speed. They also learn the best way to read<br>textbooks, take notes, and study for tests. As a result, students complete homework more quickly and easily, get better grades, and enjoy<br>reading more.</div>
  </section>

  <footer class="contact">
    For More Information or to Register Call 1-800-555-0142<br>
    Mon.-Fri. 5am–7pm, Sat. 5am–4pm and Sun. 6am–4pm&nbsp; Please see reverse side for program schedule.
  </footer>
</main>
</body>
</html>
```